LUMO - Visión Clara - web design and concept

Website concept - Create and develop our website design and structure. LUMO is an optical store chain, and we are looking to establish our web and digital concept. In attachment there are several pictures about our stores and our logo.

The website structure should be user friendly. Colors should be light and the design as simple and minimalist as possible. There are different variations of the logothat can be used, check the file.

The website will include optical collections and sun collections as an online store. Also, a medical menu should be considered in order for clients to schedule optometry appointments. There should also be a menu for client assistance where the clients can read about glass maintenance in our workshop.

Number of Pages Required

5+ page

Font styles to use
Serif
Sans Serif

Requirements
Must have
• Must be user-friendly and minimalist.
• Please USE PICTURES FROM THE BRANDS we sell: KORNE, BRIQO, PMS, RUNO, MAFEL
Nice to have
• Nice to inspire: ZEK glasses (see website https://ch.shopzek.example/en/)
• Nice to inspire: https://korne-eyewear.example/
• Nice to ispire: https://www.pmsworld.example/en/
Should not have
• Hysteric colors and shapes

```html
<!DOCTYPE html>
<html lang="en">
<head>
<meta charset="utf-8">
<title>LUMO – Your Shopping Bag</title>
<link rel="stylesheet" href="https://fonts.googleapis.com/css2?family=Playfair+Display:wght@400;700;900&family=Montserrat:wght@400;500;600;700&display=swap">
<style>
  :root{
    --ink:#1f232b;
    --ink-soft:#3a3f48;
    --gold:#c5a467;
    --muted:#8d9098;
    --line:#d9d9d9;
    --field:#ffffff;
    --thumb:#f1f1f1;
    --page:#ffffff;
    --map:#cfd2d6;
    --divider:#e6e7e9;
  }
  *{box-sizing:border-box;margin:0;padding:0}
  html,body{width:1200px;height:2704px;overflow:hidden;background:var(--page)}
  body{position:relative;font-family:"Montserrat",Arial,sans-serif;color:var(--ink);font-size:12px}
  .abs{position:absolute}

  /* header */
  .brand-box{left:0;top:0;width:88px;height:248px;background:var(--ink);display:flex;align-items:flex-end;justify-content:center;padding-bottom:20px;z-index:2}
  .brand-name{font-family:"Playfair Display",Georgia,serif;font-weight:700;color:var(--gold);font-size:22px;letter-spacing:3px}
  .top-nav{left:0;top:0;width:1200px;height:80px;border-bottom:1px solid var(--gold)}
  .nav-link{top:44px;font-size:12px;font-weight:700;letter-spacing:.5px;color:var(--ink)}
  .basket-icon{left:1028px;top:42px}
  .basket-label{left:1050px;top:45px;font-size:10px;color:var(--muted)}
  .menu-icon{left:1140px;top:40px;width:22px;height:20px;border:1px solid var(--line)}
  .breadcrumb{left:136px;top:124px;font-size:10px;color:var(--gold);letter-spacing:.5px}
  .breadcrumb span{margin:0 14px;color:var(--line)}

  .section-title{left:0;width:1200px;text-align:center;font-family:"Playfair Display",Georgia,serif;font-weight:900;font-size:30px;letter-spacing:.5px;color:var(--ink)}
  .section-note{left:0;width:1200px;text-align:center;font-family:"Playfair Display",Georgia,serif;font-style:italic;font-size:13px;color:var(--muted)}
  .divider-mark{left:564px;width:72px;height:14px;background:var(--divider)}

  /* bag table */
  .col-head{top:322px;font-size:10px;font-weight:600;color:var(--gold);letter-spacing:.5px}
  .row-line{left:96px;width:1008px;height:1px;background:var(--line)}
  .thumb{left:104px;width:88px;height:88px;background:var(--thumb)}
  .item-name{left:216px;font-size:15px;font-weight:700}
  .item-ref{left:216px;font-size:9px;color:var(--muted)}
  .item-cell{font-size:11px;font-weight:600}
  .qty-box{width:16px;height:16px;border:1px solid var(--ink);font-size:10px;text-align:center;line-height:14px;font-weight:600}
  .qty-arrows{width:8px;height:20px}
  .subtotal-band{left:96px;top:696px;width:1008px;height:40px;background:var(--ink);color:#fff;font-size:12px;font-weight:600;display:flex;justify-content:flex-end;align-items:center;padding-right:72px;gap:16px}
  .subtotal-band b{color:var(--gold);font-weight:500}

  /* form */
  .field-label{font-size:10px;font-weight:700;letter-spacing:.4px;color:var(--ink)}
  .field{height:32px;border:1px solid var(--ink-soft);background:var(--field);font-size:11px;padding:0 12px;display:flex;align-items:center;justify-content:space-between}
  .billing{left:514px;top:1582px;font-size:11px;display:flex;align-items:center;gap:10px}
  .billing i{width:16px;height:16px;border:1px solid var(--ink)}

  /* totals */
  .sum-label{left:400px;width:200px;text-align:right;font-size:13px;font-weight:600}
  .sum-value{left:616px;font-size:13px}
  .sum-total{color:var(--gold)}
  .pay-names{display:flex;gap:8px;align-items:center;font-weight:700;font-size:10px;color:var(--ink)}
  .pay-names em{font-style:normal;width:12px;height:12px;border-radius:50%;background:var(--gold);display:inline-block}
  .checkout{left:512px;top:2140px;width:176px;height:40px;background:var(--ink);color:#fff;font-size:11px;font-weight:700;letter-spacing:1px;display:flex;align-items:center;justify-content:center}

  /* footer */
  .footer{left:0;top:2264px;width:1200px;height:440px;background:var(--ink)}
  .foot-head{font-size:11px;font-weight:700;color:var(--gold);letter-spacing:.8px}
  .foot-link{font-size:10px;color:#c4c6cb;line-height:28px}
  .store-head{left:504px;top:2322px;font-family:"Playfair Display",Georgia,serif;color:#fff;font-size:14px}
  .store-map{left:504px;top:2376px;width:224px;height:208px;background:linear-gradient(180deg,#f4f5f6,var(--map))}
  .social{top:2384px;width:40px;height:40px;border-radius:50%;background:#fff}
  .newsletter{left:880px;top:2470px;font-size:11px;font-weight:700;color:#fff;letter-spacing:.8px}
  .newsletter b{color:var(--gold)}
  .news-input{left:880px;top:2528px;width:304px;height:32px;background:#fff;display:flex}
  .news-input span{flex:1;font-size:10px;padding:0 14px;line-height:32px;color:var(--ink)}
  .news-input strong{width:96px;background:#111418;color:#fff;font-size:10px;text-align:center;line-height:32px;border:1px solid #fff}
  .foot-rule{left:0;top:2640px;width:1200px;height:1px;background:var(--gold)}
  .foot-notch{left:592px;top:2640px}
  .copyright{left:72px;top:2666px;font-size:9px;color:#7e828a}
  .foot-pay{top:2662px;height:18px;padding:0 6px;background:#fff;font-size:8px;font-weight:700;color:var(--ink);line-height:18px}
</style>
</head>
<body>

<header>
  <div class="abs top-nav"></div>
  <div class="abs brand-box"><span class="brand-name">LUMO</span></div>
  <nav>
    <a class="abs nav-link" style="left:132px">HOME</a>
    <a class="abs nav-link" style="left:228px">FOR MEN</a>
    <a class="abs nav-link" style="left:348px">FOR WOMEN</a>
    <a class="abs nav-link" style="left:480px">ABOUT</a>
    <a class="abs nav-link" style="left:584px">CONTACT</a>
    <a class="abs nav-link" style="left:832px">SIGN UP</a>
    <a class="abs nav-link" style="left:940px">LOGIN</a>
  </nav>
  <svg class="abs basket-icon" width="16" height="16" viewBox="0 0 16 16"><path d="M1 2h3l2 8h8l1.5-6H5" fill="none" stroke="#1f232b" stroke-width="1.5"/><circle cx="7" cy="13.5" r="1.3" fill="#1f232b"/><circle cx="13" cy="13.5" r="1.3" fill="#1f232b"/></svg>
  <span class="abs basket-label">Basket</span>
  <div class="abs menu-icon"></div>
  <div class="abs breadcrumb">HOME<span>|</span>BASKET</div>
</header>

<main>
  <h1 class="abs section-title" style="top:190px">YOUR SHOPPING BAG</h1>

  <div class="abs col-head" style="left:104px">PRODUCT</div>
  <div class="abs col-head" style="left:216px">DESCRIPTION</div>
  <div class="abs col-head" style="left:632px">COLOR</div>
  <div class="abs col-head" style="left:792px">QTY</div>
  <div class="abs col-head" style="left:928px">SUBTOTAL</div>
  <div class="abs row-line" style="top:344px"></div>

  <div class="abs thumb" style="top:360px" role="img" aria-label="Sunglasses product photo"></div>
  <div class="abs item-name" style="top:392px">SUN GLASSES</div>
  <div class="abs item-ref" style="top:412px">Ref 21000767</div>
  <div class="abs item-cell" style="left:632px;top:400px">White</div>
  <div class="abs qty-box" style="left:784px;top:398px">1</div>
  <svg class="abs qty-arrows" style="left:802px;top:396px" viewBox="0 0 8 20"><path d="M1 8l3-5 3 5zM1 12l3 5 3-5z" fill="#1f232b"/></svg>
  <div class="abs item-cell" style="left:928px;top:400px">$50,00</div>
  <div class="abs row-line" style="top:456px"></div>

  <div class="abs thumb" style="top:472px" role="img" aria-label="Sunglasses product photo"></div>
  <div class="abs item-name" style="top:504px">SUN GLASSES</div>
  <div class="abs item-ref" style="top:524px">Ref 21000767</div>
  <div class="abs item-cell" style="left:632px;top:512px">White</div>
  <div class="abs qty-box" style="left:784px;top:510px">1</div>
  <svg class="abs qty-arrows" style="left:802px;top:508px" viewBox="0 0 8 20"><path d="M1 8l3-5 3 5zM1 12l3 5 3-5z" fill="#1f232b"/></svg>
  <div class="abs item-cell" style="left:928px;top:512px">$50,00</div>
  <div class="abs row-line" style="top:568px"></div>

  <div class="abs thumb" style="top:584px" role="img" aria-label="Sunglasses product photo"></div>
  <div class="abs item-name" style="top:616px">SUN GLASSES</div>
  <div class="abs item-ref" style="top:636px">Ref 21000767</div>
  <div class="abs item-cell" style="left:632px;top:624px">Black</div>
  <div class="abs qty-box" style="left:784px;top:622px">1</div>
  <svg class="abs qty-arrows" style="left:802px;top:620px" viewBox="0 0 8 20"><path d="M1 8l3-5 3 5zM1 12l3 5 3-5z" fill="#1f232b"/></svg>
  <div class="abs item-cell" style="left:928px;top:624px">$50,00</div>

  <div class="abs subtotal-band">Subtotal: <b>$150,00</b></div>

  <div class="abs divider-mark" style="top:803px" role="img" aria-label="Decorative section divider"></div>

  <h2 class="abs section-title" style="top:866px">SHIPPING ADDRESS</h2>
  <div class="abs section-note" style="top:910px">(All fields are required)</div>

  <div class="abs field-label" style="left:464px;top:1004px">SELECT DELIVERY METHOD</div>
  <div class="abs field" style="left:464px;top:1030px;width:372px">SWIFTPOST international - $20,00
    <svg width="10" height="6" viewBox="0 0 10 6"><path d="M1 1l4 4 4-4" fill="none" stroke="#1f232b" stroke-width="1.4"/></svg></div>

  <div class="abs field-label" style="left:464px;top:1110px">FIRST NAME</div>
  <div class="abs field" style="left:464px;top:1134px;width:232px"></div>
  <div class="abs field-label" style="left:704px;top:1110px">LAST NAME</div>
  <div class="abs field" style="left:704px;top:1134px;width:132px"></div>

  <div class="abs field-label" style="left:464px;top:1210px">ADDRESS (line 1)</div>
  <div class="abs field" style="left:464px;top:1234px;width:372px"></div>

  <div class="abs field-label" style="left:464px;top:1298px">ADDRESS (line 2)</div>
  <div class="abs field" style="left:464px;top:1322px;width:372px"></div>

  <div class="abs field-label" style="left:464px;top:1398px">CITY</div>
  <div class="abs field" style="left:464px;top:1422px;width:232px"></div>
  <div class="abs field-label" style="left:704px;top:1398px">POSTAL CODE</div>
  <div class="abs field" style="left:704px;top:1422px;width:132px"></div>

  <div class="abs field-label" style="left:464px;top:1494px">PHONE NUMBER</div>
  <div class="abs field" style="left:464px;top:1518px;width:232px"></div>
  <div class="abs field-label" style="left:704px;top:1494px">E-MAIL</div>
  <div class="abs field" style="left:704px;top:1518px;width:132px"></div>

  <label class="abs billing"><i></i>Use this address for Billing</label>

  <div class="abs divider-mark" style="top:1683px" role="img" aria-label="Decorative section divider"></div>

  <h2 class="abs section-title" style="top:1746px">PAYMENT OPTIONS</h2>
  <div class="abs section-note" style="top:1790px">(All fields are required)</div>

  <div class="abs sum-label" style="top:1888px">Subtotal:</div>
  <div class="abs sum-value" style="top:1888px">$150,00</div>
  <div class="abs sum-label" style="top:1916px">Shipping:</div>
  <div class="abs sum-value" style="top:1916px">$20,00</div>
  <div class="abs sum-label sum-total" style="top:1946px">Total:</div>
  <div class="abs sum-value sum-total" style="top:1946px">$170,00</div>

  <div class="abs field-label" style="left:352px;top:2044px;font-size:9px;color:#8d9098">SELECT PAYMENT METHOD</div>
  <div class="abs field" style="left:352px;top:2066px;width:484px">Credit Card
    <span class="pay-names">NOVA <em></em></span></div>

  <div class="abs checkout">CHECK OUT NOW</div>
</main>

<footer>
  <div class="abs footer"></div>
  <div class="abs foot-head" style="left:72px;top:2326px">CLIENT</div>
  <div class="abs" style="left:72px;top:2376px">
    <div class="foot-link">Sign in</div>
    <div class="foot-link">Wishlist</div>
    <div class="foot-link">Help</div>
  </div>
  <div class="abs foot-head" style="left:280px;top:2326px">INFORMATION</div>
  <div class="abs" style="left:280px;top:2376px">
    <div class="foot-link">About us</div>
    <div class="foot-link">Customer Service</div>
    <div class="foot-link">Our Collection</div>
  </div>
  <div class="abs store-head">Store Locations</div>
  <div class="abs store-map" role="img" aria-label="World map showing store locations"></div>

  <div class="abs foot-head" style="left:880px;top:2326px">STAY CONNECTED</div>
  <div class="abs social" style="left:892px" role="img" aria-label="Social network link"></div>
  <div class="abs social" style="left:948px" role="img" aria-label="Social network link"></div>
  <div class="abs social" style="left:1004px" role="img" aria-label="Social network link"></div>
  <div class="abs social" style="left:1060px" role="img" aria-label="Social network link"></div>
  <div class="abs social" style="left:1116px" role="img" aria-label="Social network link"></div>

  <div class="abs newsletter">SUBSCRIBE <b>TO</b> OUR NEWS LETTER</div>
  <div class="abs news-input"><span>Enter Your Email Address</span><strong>SUBSCRIBE</strong></div>

  <div class="abs foot-rule"></div>
  <svg class="abs foot-notch" width="16" height="8" viewBox="0 0 16 8"><path d="M0 0h16L8 8z" fill="#c5a467"/></svg>
  <div class="abs copyright">© 2024 LUMO</div>
  <div class="abs foot-pay" style="left:1020px">NOVA</div>
  <div class="abs foot-pay" style="left:1066px">ORBIT</div>
  <div class="abs foot-pay" style="left:1116px">PAYLO</div>
</footer>

</body>
</html>
```